young adult fiction novel titled 'Chronicles of the Orrery - The Heron's Song'

Introduction
Hello! Attached you will find a combination of my own amateurish attempts at graphic design and also pictures that have inspired me. With the obvious exception of the ‘Crown of Embers’ and ‘Keeper of the Vales’ stuff, I have purchased the other images so they are fair game to be used (contact me if you want the hi-res versions).
I hope that by showing you these, I might be able to convey what I’m looking for in a front cover and a website. I’d just like to make a few points that might also help you understand a little better.
1. The book is called ‘The Heron’s Song’. It is a 'knights of the round table' type story so I would like
2. My concept is 12 tales, each told by a member of the zodiac. I would like the first front cover to be designed in such a way that the following 11 can be thematically linked together. The Heron’s Song is obviously the Capricorn’s tale.
3. As Capricorn is an earth sign, I would like the colour scheme to be green and brown. I would also definitely like the motto to be ‘Lift the Tide Higher’.
4. The name of the series will be ‘Chronicles of the Orrery’ and I would like this written somewhere on the front cover.
5. My Nom de Plume is going to be RM Tollingsby.
6. There is room for quirkiness in the design. The book itself is, I may say so, dryly humourous and, also, is set in the future. This allows for a slight twist on more traditional heraldry.
7. It would be nice to include a stylised zodiac wheel that could appear on all the books and the website. It would be one of the motifs that links the books together. In the story, a round table of the zodiac is set up. This is a fusion of astrology and Arthurian legend.
8. My main concern with my own design is the colouring. I was concerned that it looked a little cheap to have a single matt colour. I was thinking that some sort of texture of w/e might add a bit of quality to the design. This is not a deal breaker and, as I said, I would regard it as a safe option if the above change is made.
9. My perfect design would be more like an ACTUAL shield with elements of classic heraldry but a a subtle nod to dystopian iron dust / ember trials type art work.
Updates
Reason: I have one very strong contender but several other strong drafts on the table and want to give them a chance to improve their designs.
Target Market(s)
Western Teenagers who read fantasy novels such as KOTV, crown of embers, Milo Brackwell etc
Industry/Entity Type
Graphic Design

```html
<!DOCTYPE html>
<html lang="en">
<head>
<meta charset="utf-8">
<title>Chronicles of the Orrery – The Heron’s Song – Cover Wrap</title>
<link rel="stylesheet" href="https://fonts.googleapis.com/css2?family=Cinzel:wght@400;500&family=Cormorant+Garamond:ital,wght@1,500&family=Noto+Sans+Symbols&display=swap">
<style>
  :root {
    --paper: #ffffff;
    --cloth: #6b8461;
    --cloth-edge: #7c9472;
    --ornament: #65805b;
    --parchment: #d9dcc2;
    --ochre: #d29b67;
    --glyph: #6b8461;
  }
  * { margin: 0; padding: 0; box-sizing: border-box; }
  html, body {
    width: 1200px; height: 891px; overflow: hidden;
    background: var(--paper);
  }
  .wrap {
    position: absolute; left: 6px; top: 41px;
    width: 1188px; height: 823px;
    background: var(--cloth);
  }
  .panel { position: absolute; top: 0; height: 100%; }
  .back-cover { left: 0; width: 548px; }
  .spine {
    left: 548px; width: 90px;
    border-left: 1.5px solid var(--cloth-edge);
    border-right: 1.5px solid var(--cloth-edge);
  }
  .front-cover { left: 638px; width: 550px; }

  .corner-ornament {
    position: absolute; width: 140px; height: 120px;
    background: var(--ornament); opacity: .55; border-radius: 40px;
  }
  .corner-ornament.tl { top: 12px; left: 14px; }
  .corner-ornament.tr { top: 12px; right: 14px; }
  .corner-ornament.bl { bottom: 12px; left: 14px; }
  .corner-ornament.br { bottom: 12px; right: 14px; }

  .spine-text {
    position: absolute; top: 78px; left: 50%;
    transform: translateX(-50%);
    writing-mode: vertical-rl;
    display: flex; align-items: center; gap: 16px;
    font-family: "Cinzel", serif; color: var(--parchment);
    white-space: nowrap;
  }
  .spine-author { font-size: 23px; letter-spacing: 1px; }
  .spine-series { font-size: 14px; letter-spacing: .5px; }
  .spine-title { font-size: 25px; letter-spacing: 1px; }

  .author {
    position: absolute; top: 32px; left: 0; width: 100%;
    text-align: center; font-family: "Cinzel", serif;
    font-size: 31px; letter-spacing: 1.5px; color: var(--parchment);
  }
  .zodiac-wheel {
    position: absolute; left: 85px; top: 127px;
    width: 400px; height: 400px;
  }
  .sign {
    font-family: "Noto Sans Symbols", sans-serif;
    font-size: 30px; fill: var(--glyph);
    text-anchor: middle; dominant-baseline: central;
  }
  .motto {
    position: absolute; top: 580px; left: 0; width: 100%;
    text-align: center; font-family: "Cormorant Garamond", serif;
    font-style: italic; font-weight: 500; font-size: 16px;
    color: var(--ochre);
  }
  .series {
    position: absolute; top: 676px; left: 0; width: 100%;
    text-align: center; font-family: "Cinzel", serif;
    font-size: 29px; letter-spacing: 1px; color: var(--parchment);
  }
  .title {
    position: absolute; top: 712px; left: 0; width: 100%;
    text-align: center; font-family: "Cinzel", serif;
    font-size: 48px; letter-spacing: 1.5px; color: var(--parchment);
  }
</style>
</head>
<body>
<main class="wrap">
  <section class="panel back-cover">
    <div class="corner-ornament tl" role="img" aria-label="Faint scrollwork corner ornament"></div>
    <div class="corner-ornament tr" role="img" aria-label="Faint scrollwork corner ornament"></div>
    <div class="corner-ornament bl" role="img" aria-label="Faint scrollwork corner ornament"></div>
    <div class="corner-ornament br" role="img" aria-label="Faint scrollwork corner ornament"></div>
  </section>

  <section class="panel spine">
    <div class="spine-text">
      <span class="spine-author">R.M. Tollingsby</span>
      <span class="spine-series">Chronicles of the Orrery:</span>
      <span class="spine-title">The Heron’s Song</span>
    </div>
  </section>

  <section class="panel front-cover">
    <div class="corner-ornament tl" role="img" aria-label="Faint scrollwork corner ornament"></div>
    <div class="corner-ornament tr" role="img" aria-label="Faint scrollwork corner ornament"></div>
    <div class="corner-ornament bl" role="img" aria-label="Faint scrollwork corner ornament"></div>
    <div class="corner-ornament br" role="img" aria-label="Faint scrollwork corner ornament"></div>

    <h2 class="author">R.M. Tollingsby</h2>

    <svg class="zodiac-wheel" viewBox="-200 -200 400 400" aria-label="Zodiac wheel with Capricorn highlighted">
      <circle class="ring" r="168.5" fill="none" stroke="var(--parchment)" stroke-width="57"
              stroke-dasharray="82.2 6" stroke-dashoffset="-3"/>
      <circle class="ring-active" r="168.5" fill="none" stroke="var(--ochre)" stroke-width="57"
              stroke-dasharray="82.2 976.5" stroke-dashoffset="-708.8"/>
      <text class="sign" x="162.8" y="43.6">&#x264D;&#xFE0E;</text>
      <text class="sign" x="119.1" y="119.1">&#x264C;&#xFE0E;</text>
      <text class="sign" x="43.6" y="162.8">&#x264B;&#xFE0E;</text>
      <text class="sign" x="-43.6" y="162.8">&#x264A;&#xFE0E;</text>
      <text class="sign" x="-119.1" y="119.1">&#x2649;&#xFE0E;</text>
      <text class="sign" x="-162.8" y="43.6">&#x2648;&#xFE0E;</text>
      <text class="sign" x="-162.8" y="-43.6">&#x2653;&#xFE0E;</text>
      <text class="sign" x="-119.1" y="-119.1">&#x2652;&#xFE0E;</text>
      <text class="sign" x="-43.6" y="-162.8">&#x2651;&#xFE0E;</text>
      <text class="sign" x="43.6" y="-162.8">&#x2650;&#xFE0E;</text>
      <text class="sign" x="119.1" y="-119.1">&#x264F;&#xFE0E;</text>
      <text class="sign" x="162.8" y="-43.6">&#x264E;&#xFE0E;</text>
      <rect class="emblem" x="-68" y="-112" width="128" height="212" rx="44"
            fill="var(--ochre)" role="img" aria-label="Stylised Capricorn goat head emblem in profile"/>
    </svg>

    <p class="motto">“Lift the Tide Higher.”</p>
    <p class="series">Chronicles of the Orrery:</p>
    <h1 class="title">The Heron’s Song</h1>
  </section>
</main>
</body>
</html>
```